Jewelers Website

This is for the DESIGN ONLY.
I am a software programmer and will be doing the development.
New website design for
www.lunagemcraft.com.au
Need a fresh new look for an online only jewellery business who produce their jewellery by hand. I would like it designed in a parallax style. Feel free to recommend fonts to use for the site. This is an Australian based company located in NSW so shots of sites in NSW might make nice background images.
http://plaxorin.me/demo/#theme=parallax
To contain the below sections
About Us
Contact Us
Gallery
Testimonials
Diamond Types
The colour scheme is to be Black / White and Silver.
With the Parallax style there will be moving sections and images for added impact.
Target Market(s)
Young Adults mainly engagement jewellery

```html
<!DOCTYPE html>
<html lang="en">
<head>
<meta charset="utf-8">
<title>Luna Gemcraft</title>
<link rel="stylesheet" href="https://fonts.googleapis.com/css2?family=Open+Sans:wght@300;400;600&display=swap">
<style>
  :root {
    --ink: #2b2b2b;
    --header-bg: #2a2a2a;
    --dark-band: #2f2f2f;
    --footer-bg: #3a3a3a;
    --paper: #ffffff;
    --mist: #ececec;
    --silver: #c9c9c9;
    --silver-dark: #8f8f8f;
    --text: #555555;
    --muted: #8a8a8a;
    --white: #ffffff;
    --field-line: #cfcfcf;
    --button: #3d3d3d;
  }
  * { box-sizing: border-box; margin: 0; padding: 0; }
  html, body { width: 1200px; height: 3404px; overflow: hidden; }
  body { position: relative; background: var(--paper); font-family: "Open Sans", Arial, sans-serif; color: var(--text); }
  section, header, footer { position: absolute; left: 0; width: 1200px; }

  /* Header */
  .site-header { top: 0; height: 163px; background: var(--header-bg); }
  .brand { position: absolute; left: 87px; top: 44px; color: var(--white); font-weight: 400; font-size: 31px; line-height: 36px; letter-spacing: 1px; }
  .main-nav { position: absolute; right: 89px; top: 84px; display: flex; gap: 38px; }
  .main-nav a { color: var(--white); text-decoration: none; font-size: 17px; }

  /* Hero */
  .hero { top: 163px; height: 563px; background: linear-gradient(110deg, #1d1d1d 0%, #4a4a4a 35%, #7a7a7a 55%, #3a3a3a 80%, #2a2a2a 100%); }
  .hero-photo { position: absolute; inset: 0; }
  .hero-badge { position: absolute; left: 830px; top: 119px; width: 266px; height: 266px; border-radius: 50%; background: rgba(30,30,30,0.88); color: var(--white); text-align: center; }
  .hero-badge .big { margin-top: 52px; font-size: 44px; font-weight: 300; letter-spacing: 2px; }
  .hero-badge .sub { margin-top: 8px; font-size: 26px; font-weight: 300; }
  .hero-badge .cta { margin-top: 22px; font-size: 15px; display: flex; justify-content: center; align-items: center; gap: 12px; }
  .dots { position: absolute; display: flex; gap: 6px; }
  .dots span { width: 15px; height: 15px; border-radius: 50%; background: #bdbdbd; }
  .dots span.on { background: var(--white); }
  .hero .dots { left: 1026px; top: 522px; }

  /* Section headings */
  .section-title { position: absolute; left: 0; width: 100%; text-align: center; font-weight: 300; font-size: 38px; letter-spacing: 1px; }
  .divider { position: absolute; left: 516px; width: 168px; height: 14px; }
  .divider::before { content: ""; position: absolute; left: 0; right: 0; top: 6px; height: 1px; background: currentColor; }
  .divider::after { content: ""; position: absolute; left: 78px; top: 1px; width: 11px; height: 11px; background: currentColor; transform: rotate(45deg); }

  /* About */
  .about { top: 726px; height: 464px; background: var(--paper); color: var(--ink); }
  .about .section-title { top: 48px; color: #444; }
  .about .divider { top: 100px; color: #555; }
  .about-ring { position: absolute; left: 89px; top: 153px; width: 370px; height: 191px; background: radial-gradient(ellipse at 50% 45%, #f2f2f2 0%, #c4c4c4 45%, #ffffff 75%); }
  .about-copy { position: absolute; left: 499px; top: 170px; width: 617px; font-size: 13px; line-height: 21px; color: var(--text); }
  .about-copy p + p { margin-top: 10px; }

  /* Gallery */
  .gallery { top: 1190px; height: 535px; background: linear-gradient(180deg, #3a3a3a 0%, #262626 60%, #303030 100%); color: var(--white); }
  .gallery .section-title { top: 68px; }
  .gallery .divider { top: 122px; color: var(--white); }
  .gallery-grid { position: absolute; left: 0; top: 0; }

  /* Testimonials */
  .testimonials { top: 1725px; height: 471px; background: var(--mist); color: var(--ink); }
  .testimonials h2 { position: absolute; top: 50px; width: 100%; text-align: center; font-weight: 400; font-size: 34px; color: #222; }
  .avatar { position: absolute; left: 524px; top: 124px; width: 144px; height: 144px; border-radius: 50%; border: 5px solid var(--white); background: linear-gradient(160deg, #e6d2c0, #b89a84); box-shadow: 0 2px 6px rgba(0,0,0,0.2); }
  .quote { position: absolute; top: 298px; width: 100%; text-align: center; font-size: 17px; line-height: 31px; color: #444; }
  .quote-author { position: absolute; top: 368px; right: 143px; font-size: 15px; color: #555; }
  .testimonials .dots { left: 560px; top: 416px; }
  .testimonials .dots span { width: 13px; height: 13px; background: #c4c4c4; }
  .testimonials .dots span.on { background: #555; }

  /* Jewelry types */
  .types { top: 2196px; height: 538px; background: linear-gradient(180deg, #3c3c3c 0%, #1f1f1f 70%, #2c2c2c 100%); color: var(--white); }
  .types .section-title { top: 70px; font-size: 34px; }
  .types .divider { top: 145px; color: var(--white); }
  .type-card { position: absolute; top: 237px; width: 295px; height: 202px; border: 6px solid #6a6a6a; }
  .type-card.aqua { left: 87px; background: radial-gradient(ellipse at 45% 50%, #6fd0dc 0%, #3a8f9a 25%, #bdbdbd 45%, #4a4a4a 100%); }
  .type-card.pave { left: 448px; background: radial-gradient(ellipse at 50% 50%, #e8e8e8 0%, #9a9a9a 35%, #111 75%); }
  .type-card.trio { left: 813px; background: radial-gradient(ellipse at 50% 50%, #d8d8d8 0%, #7a7a7a 30%, #0c0c0c 70%); }

  /* Contact */
  .contact { top: 2734px; height: 553px; background: var(--paper); color: var(--ink); }
  .contact .section-title { top: 50px; color: #333; }
  .contact .divider { top: 103px; color: #555; }
  .field { position: absolute; left: 138px; width: 445px; border: 1px solid var(--field-line); font-size: 13px; color: #555; padding: 13px 14px; }
  .field.name { top: 176px; height: 46px; }
  .field.email { top: 242px; height: 46px; }
  .field.message { top: 308px; height: 110px; }
  .send { position: absolute; left: 474px; top: 446px; width: 109px; height: 48px; background: var(--button); color: var(--white); font-size: 17px; letter-spacing: 1px; display: flex; align-items: center; justify-content: center; }
  .map { position: absolute; left: 683px; top: 176px; width: 402px; height: 163px; background: linear-gradient(135deg, #e9e6dc, #d9d4c5 60%, #e4e0d4); }
  .info { position: absolute; font-size: 14px; line-height: 29px; color: #555; display: flex; gap: 14px; }
  .info svg { flex: none; margin-top: 7px; }
  .info.addr { left: 685px; top: 385px; }
  .info.mail { left: 918px; top: 385px; }
  .info.phone { left: 918px; top: 433px; }

  /* Footer */
  .site-footer { top: 3287px; height: 117px; background: var(--footer-bg); color: var(--white); font-size: 13px; }
  .footer-links { position: absolute; left: 89px; top: 32px; }
  .copyright { position: absolute; left: 89px; top: 67px; }
  .social { position: absolute; left: 910px; top: 38px; display: flex; gap: 12px; }
  .social span { width: 36px; height: 36px; background: #5a5a5a; }
</style>
</head>
<body>

<header class="site-header">
  <div class="brand">LUNA<br>GEMCRAFT</div>
  <nav class="main-nav">
    <a href="#about">About Us</a>
    <a href="#gallery">Gallery</a>
    <a href="#testimonials">Testimonials</a>
    <a href="#types">Diamond Types</a>
    <a href="#contact">Contact Us</a>
  </nav>
</header>

<section class="hero">
  <div class="hero-photo" role="img" aria-label="Model wearing a diamond necklace and chandelier earrings on a dark background"></div>
  <div class="hero-badge">
    <div class="big">JEWELRY</div>
    <div class="sub">NEW COLLECTIONS</div>
    <div class="cta">
      <svg width="16" height="16" viewBox="0 0 16 16"><circle cx="8" cy="8" r="8" fill="#fff"/><path d="M6 4.5 L11 8 L6 11.5 Z" fill="#222"/></svg>
      ENTER SHOP
    </div>
  </div>
  <div class="dots"><span class="on"></span><span></span><span></span><span></span></div>
</section>

<section class="about" id="about">
  <h2 class="section-title">ABOUT US</h2>
  <div class="divider"></div>
  <div class="about-ring" role="img" aria-label="Diamond halo engagement ring"></div>
  <div class="about-copy">
    <p>Duis autem vel eum iriure dolor in hendrerit in vulputate velit esse molestie consequat, vel illum dolore eu feugiat nulla facilisis at vero eros et accumsan et iusto odio dignissim qui blandit praesent luptatum zzril delenit augue duis dolore te feugait nulla facilisi. Nam liber tempor cum soluta nobis eleifend option congue nihil imperdiet doming id quod mazim placerat facer possim assum. Typi non habent claritatem insitam; est usus legentis in iis qui facit eorum claritatem.</p>
    <p>Claritas est etiam processus dynamicus, qui sequitur mutationem consuetudium lectorum. Mirum est notare quam littera gothica, quam nunc putamus parum claram, anteposuerit litterarum formas humanitatis per seacula quarta decima et quinta decima. Eodem modo typi.</p>
  </div>
</section>

<section class="gallery" id="gallery">
  <h2 class="section-title">GALLERY</h2>
  <div class="divider"></div>
  <svg class="gallery-grid" width="1200" height="535" viewBox="0 0 1200 535" role="img" aria-label="Gallery of diamond close-up photographs in diamond-shaped tiles">
    <defs>
      <linearGradient id="tile" x1="0" y1="0" x2="1" y2="1">
        <stop offset="0" stop-color="#f2f2f2"/>
        <stop offset="0.5" stop-color="#a9a9a9"/>
        <stop offset="1" stop-color="#dcdcdc"/>
      </linearGradient>
    </defs>
    <g fill="url(#tile)" stroke="#ffffff" stroke-width="3">
      <polygon points="295,192 385,282 295,372 205,282"/>
      <polygon points="490,192 580,282 490,372 400,282"/>
      <polygon points="690,192 780,282 690,372 600,282"/>
      <polygon points="895,192 985,282 895,372 805,282"/>
      <polygon points="200,296 285,381 200,466 115,381"/>
      <polygon points="395,296 480,381 395,466 310,381"/>
      <polygon points="595,296 680,381 595,466 510,381"/>
      <polygon points="795,296 880,381 795,466 710,381"/>
    </g>
    <polygon points="995,296 1080,381 995,466 910,381" fill="#1a1a1a" stroke="#ffffff" stroke-width="3"/>
  </svg>
</section>

<section class="testimonials" id="testimonials">
  <h2>Loved by thousands of people world wide</h2>
  <div class="avatar" role="img" aria-label="Customer portrait"></div>
  <p class="quote">I am so happy to have met you! Before Voice Forward, I had vocal<br>problems that clouded my mind and made it zero fun to sing. Now I sing again and even have a weekly job as a speaker.</p>
  <div class="quote-author">- Tomas, Germany</div>
  <div class="dots"><span class="on"></span><span></span><span></span><span></span></div>
</section>

<section class="types" id="types">
  <h2 class="section-title">EXQUISITE JEWELRY TYPES FOR YOU</h2>
  <div class="divider"></div>
  <div class="type-card aqua" role="img" aria-label="Aquamarine ring with diamond shoulders"></div>
  <div class="type-card pave" role="img" aria-label="Pave diamond cocktail ring"></div>
  <div class="type-card trio" role="img" aria-label="Set of diamond rings on black"></div>
</section>

<section class="contact" id="contact">
  <h2 class="section-title">CONTACT US</h2>
  <div class="divider"></div>
  <div class="field name">Name</div>
  <div class="field email">Email</div>
  <div class="field message">Send your message</div>
  <div class="send">SEND</div>
  <div class="map" role="img" aria-label="Street map showing the studio location"></div>
  <div class="info addr">
    <svg width="12" height="16" viewBox="0 0 12 16"><path d="M6 0 C2.7 0 0 2.6 0 5.8 C0 10 6 16 6 16 C6 16 12 10 12 5.8 C12 2.6 9.3 0 6 0 Z" fill="#444"/><circle cx="6" cy="5.8" r="2.2" fill="#fff"/></svg>
    <div>1420 Kestrel Bay Ave.<br>Marlow NY 11290<br>Arizona</div>
  </div>
  <div class="info mail">
    <svg width="18" height="13" viewBox="0 0 18 13"><rect width="18" height="13" fill="#444"/><path d="M0 0 L9 7 L18 0" fill="none" stroke="#fff" stroke-width="1.4"/></svg>
    <div>info@lunagemcraft.com</div>
  </div>
  <div class="info phone">
    <svg width="16" height="16" viewBox="0 0 16 16"><path d="M3.5 0.5 L6 3.5 L4.5 5.5 C5.5 7.8 8.2 10.5 10.5 11.5 L12.5 10 L15.5 12.5 L13.8 15.3 C7 15 1 9 0.7 2.2 Z" fill="#444"/></svg>
    <div>89 555 0142</div>
  </div>
</section>

<footer class="site-footer">
  <div class="footer-links">Terms and Conditions | Privacy Promise | FAQ's | Contact Us</div>
  <div class="copyright">Copyright © 2013. All Rights Reserved.</div>
  <div class="social"><span></span><span></span><span></span><span></span></div>
</footer>

</body>
</html>
```